Australian Web Design company needs a business card design

We need a business card design for a Sydney based Web Design/Development company called "Tall Pine Web Design". We design, build and deploy websites for small to medium sized businesses. The final design should be clean and communicate that we are a professional and supportive company.
I'd like the Icon to be abstract. Something that embodies the power of the internet, needs to be clean/professional and show that we are human and that we support our customers. Hope that helps.
Target Market(s)
All small to medium businesses
Industry/Entity Type
Business
Contact Information for Business Card
Martin Forbes
Tall Pine Web Design
17 Wattle Grove Road
West Kelsworth
NSW 2250
0438 527 064
martin@tallpinewebdesign.com.au
www.tallpinewebdesign.com.au

```html
<!DOCTYPE html>
<html lang="en">
<head>
<meta charset="utf-8">
<title>Tall Pine Web Design – Business Card</title>
<link rel="stylesheet" href="https://fonts.googleapis.com/css2?family=Lato:wght@400;700&family=Raleway:wght@700&display=swap">
<style>
  :root {
    --brand-red: #e30613;
    --brand-red-deep: #d10510;
    --paper: #f7f5f2;
    --ink: #3a3a3a;
    --stage: #e4e4e4;
    --pattern-soft: rgba(227, 6, 19, 0.18);
    --white: #ffffff;
  }
  * { box-sizing: border-box; margin: 0; padding: 0; }
  html, body {
    width: 1200px;
    height: 900px;
    overflow: hidden;
    background: var(--stage);
  }
  .stage {
    width: 1200px;
    height: 900px;
    display: flex;
    flex-direction: column;
    align-items: center;
    justify-content: center;
    gap: 56px;
  }
  .card {
    width: 630px;
    height: 360px;
    position: relative;
    overflow: hidden;
    box-shadow: 0 6px 18px rgba(0, 0, 0, 0.18);
  }

  /* Back side */
  .card-back {
    background: linear-gradient(135deg, var(--brand-red), var(--brand-red-deep));
    display: flex;
    flex-direction: column;
    align-items: center;
    justify-content: center;
    gap: 26px;
  }
  .brand-mark {
    width: 92px;
    height: 92px;
    border: 3px solid var(--white);
    border-radius: 50%;
  }
  .brand-name {
    font-family: "Raleway", sans-serif;
    font-weight: 700;
    font-size: 30px;
    color: var(--white);
    letter-spacing: 0.3px;
  }

  /* Front side */
  .card-front {
    background: var(--paper);
    font-family: "Lato", sans-serif;
    color: var(--ink);
    padding: 50px 0 0 66px;
  }
  .person-name {
    font-size: 36px;
    font-weight: 700;
    color: var(--brand-red);
    letter-spacing: 0.5px;
    line-height: 1;
  }
  .person-role {
    font-size: 17px;
    margin-top: 6px;
  }
  .accent-rule {
    width: 42px;
    height: 4px;
    background: var(--brand-red);
    margin-top: 22px;
  }
  .contact-list {
    list-style: none;
    margin-top: 30px;
    display: grid;
    gap: 12px;
  }
  .contact-list li {
    display: flex;
    font-size: 18px;
  }
  .contact-label {
    width: 40px;
    color: var(--brand-red);
    font-weight: 700;
  }
  .network-pattern {
    position: absolute;
    right: 0;
    bottom: 0;
    width: 360px;
    height: 230px;
    background: linear-gradient(215deg, var(--pattern-soft) 0%, rgba(227, 6, 19, 0.08) 45%, rgba(227, 6, 19, 0) 80%);
  }
</style>
</head>
<body>
  <main class="stage">
    <section class="card card-back">
      <div class="brand-mark"></div>
      <div class="brand-name">Tall Pine Web Design</div>
    </section>

    <section class="card card-front">
      <h1 class="person-name">MARTIN FORBES</h1>
      <p class="person-role">Solution Advisor</p>
      <div class="accent-rule"></div>
      <ul class="contact-list">
        <li><span class="contact-label">T :</span>0438 527 064</li>
        <li><span class="contact-label">M :</span>martin@tallpinewebdesign.com.au</li>
        <li><span class="contact-label">W:</span>www.tallpinewebdesign.com.au</li>
      </ul>
      <div class="network-pattern" role="img" aria-label="Decorative red network pattern of connected dots and lines"></div>
    </section>
  </main>
</body>
</html>
```